16oz juice label for Hispanic market, tropical flavor

Create label for a ready to drink juice. This juice is for the Hispanic demographic and the American market. We want our logo to be very prominent on the label because our logo is very well know and the consumer will buy our brand over a competitor. This juice will be distributed throughout the country and will be in traditional grocery stores, convenience stores, bodegas or corner stores as well as Hispanic grocery stores. The label size is 24.25 cm x 8cm. The flavor to use for this label is Mango/Carrot.

Target Market(s)

Hispanic

Requirements
Must have
• Logo must be large. Appeal to Hispanic market.

```html
<!DOCTYPE html>
<html lang="en">
<head>
<meta charset="utf-8">
<title>Frutalia Carrot Mango – label variations</title>
<link href="https://fonts.googleapis.com/css2?family=Signika:wght@400;600;700&family=Roboto:wght@400;700&family=Lobster&display=swap" rel="stylesheet">
<style>
  :root{
    --ink:#1d1d1d;
    --panel-dark:#1b1b1b;
    --white:#ffffff;
    --green-dark:#2f5a27;
    --green:#7cb43a;
    --green-light:#cfe6a2;
    --gold-dark:#8a6a1e;
    --gold:#d9b45a;
    --gold-light:#f4e1a8;
    --brand-red:#d3121c;
    --orange:#f08a1a;
    --yellow:#ffd21f;
    --sky:#12a5e0;
  }
  *{box-sizing:border-box;margin:0;padding:0}
  html,body{width:1158px;height:1200px;overflow:hidden;background:#fff}
  .sheet{width:1447px;height:1500px;transform:scale(0.8);transform-origin:0 0;position:relative}
  .label{position:absolute;left:0;width:1447px;height:478px;background:var(--panel-dark);overflow:hidden;font-family:"Roboto",Arial,sans-serif}
  .label--one{top:0}
  .label--two{top:511px}
  .label--three{top:1022px}

  /* left panel */
  .info{position:absolute;left:0;top:0;width:447px;height:410px;background:var(--panel-dark);color:var(--white)}
  .label--two .info{background:linear-gradient(180deg,var(--green-light) 0,#fff 70px);color:var(--ink)}
  .facts{position:absolute;left:37px;top:30px;width:286px;height:246px;background:#fff;border:1px solid #333;padding:3px 8px;color:#111;font-size:9.5px}
  .facts h2{font-weight:700;font-size:21px;line-height:23px}
  .facts .row{display:flex;border-bottom:1px solid #444;line-height:13px;white-space:nowrap}
  .facts .row span:nth-child(1){flex:0 0 160px}
  .facts .row span:nth-child(2){flex:0 0 52px}
  .facts .row span:nth-child(3){flex:1;text-align:right;padding-right:10px}
  .facts .row .wide{flex:1 !important;text-align:right;padding-right:8px}
  .facts .row.indent span:first-child{padding-left:18px}
  .facts .row.top{border-bottom:none;justify-content:space-between}
  .facts .row.top span{flex:none !important}
  .facts .head{font-weight:700;border-bottom:2px solid #111;justify-content:space-between}
  .facts .head span{flex:none !important;padding:0 !important}
  .facts .note{line-height:14px;margin-top:2px}
  .ingredients{position:absolute;left:343px;top:275px;width:250px;transform:rotate(-90deg);transform-origin:0 0;font-size:10.5px;line-height:14px;color:inherit}
  .usage{position:absolute;left:36px;top:288px;width:372px;font-size:15px;line-height:19.5px}
  .usage p+p{margin-top:19px}
  .claim{position:absolute;left:0;top:410px;width:470px;height:68px;background:linear-gradient(90deg,var(--green-dark),var(--green));border-top-right-radius:60px;color:#fff;font-family:"Signika",sans-serif;font-weight:600;font-size:20px;line-height:29px;text-align:center;padding:4px 40px 0 0}
  .label--three .claim{background:linear-gradient(90deg,var(--gold-dark),var(--gold-light) 60%,var(--gold));color:var(--ink)}

  /* centre panel */
  .front{position:absolute;left:447px;top:0;width:560px;height:478px;background:radial-gradient(circle at 60% 40%,#2c2c2c,#161616);border-top-left-radius:70px;border-left:4px solid var(--gold);overflow:hidden}
  .label--three .front{border-left-color:var(--green)}
  .front svg{position:absolute;left:0;top:0}
  .badge-new{position:absolute;left:12px;top:45px;width:130px;height:78px;border-radius:8px;background:linear-gradient(180deg,var(--gold-light),var(--gold));display:flex;align-items:center;justify-content:center;font-family:"Lobster",cursive;font-size:50px;color:var(--brand-red)}
  .label--three .badge-new{color:var(--yellow);-webkit-text-stroke:1.5px var(--brand-red)}
  .brand{position:absolute;left:150px;top:75px;font-family:"Signika",sans-serif;font-weight:700;font-size:96px;color:var(--brand-red);letter-spacing:-2px}
  .flavour{position:absolute;right:30px;top:195px;font-family:"Lobster",cursive;font-size:66px;line-height:58px;text-align:right;color:var(--gold)}
  .label--three .flavour{right:auto;left:50px;top:245px;font-size:64px}
  .fruit{position:absolute}
  .seal{position:absolute;left:358px;top:345px;width:130px;height:130px;border-radius:50%;background:#fff;border:6px solid var(--brand-red)}

  /* right panel */
  .benefits{position:absolute;left:1000px;top:0;width:447px;height:478px;background:var(--panel-dark);color:#fff;font-family:"Signika",sans-serif}
  .label--two .benefits{background:linear-gradient(180deg,var(--green-light) 60px,#fff 220px);color:var(--ink)}
  .label--three .benefits{border-left:8px solid var(--sky);border-top-left-radius:60px}
  .benefits h2{height:72px;background:linear-gradient(90deg,var(--green-dark),var(--green) 40%,var(--green));border-top-left-radius:60px;font-weight:600;font-size:26px;line-height:30px;text-align:center;padding:6px 0 0 40px;color:#fff}
  .label--three .benefits h2{background:linear-gradient(90deg,var(--gold-dark),var(--gold-light) 50%,var(--gold));color:var(--ink)}
  .benefits ul{list-style:none;margin:6px 0 0 40px;font-size:15px;line-height:24px}
  .benefits li::before{content:"• "}
  .serve{position:absolute;left:22px;top:200px;font-size:32px;line-height:40px;font-weight:400}
  .bin{position:absolute;left:345px;top:212px;width:58px;height:86px}
  .maker{position:absolute;left:235px;top:325px;font-size:22px;line-height:26px;font-weight:600;white-space:nowrap}
</style>
</head>
<body>
<div class="sheet">

  <!-- label variant 1 -->
  <section class="label label--one">
    <div class="info">
      <div class="facts">
        <h2>Supplement Facts</h2>
        <div class="row top"><span>Serving size 1 teaspoon (5ml)</span><span>Servings per container 45</span></div>
        <div class="row head"><span>Amount per Serving</span><span>% Daily Value</span></div>
        <div class="row"><span>Calories</span><span>40</span><span></span></div>
        <div class="row"><span>Calories from Fat</span><span>40</span><span></span></div>
        <div class="row"><span>Total Fat</span><span>4.5g</span><span>7.0%*</span></div>
        <div class="row indent"><span>Saturated Fat</span><span>1.0g</span><span>5.0%*</span></div>
        <div class="row indent"><span>Polyunsaturated Fat</span><span>2.0g</span><span>*</span></div>
        <div class="row indent"><span>Monounsaturated Fat</span><span>1.0g</span><span>*</span></div>
        <div class="row"><span>Cholesterol</span><span>15mg</span><span>5.0%*</span></div>
        <div class="row"><span>Total Frutalia Fatty Acids</span><span class="wide">1400-1700 mg</span></div>
        <div class="row indent"><span>Eicosapentaenoic Acid (EPA)</span><span class="wide">740-825 mg</span></div>
        <div class="row indent"><span>Docosahexaenoic Acid (DHA)</span><span class="wide">460-550 mg</span></div>
        <div class="row indent"><span>Other Frutalia Fatty Acids</span><span class="wide">200-325 mg</span></div>
        <p class="note">*Percent daily values are based on a 2000 calorie diet.<br>Daily value not established.</p>
      </div>
      <p class="ingredients">INGREDIENTS: purified, molecularly-distilled pharmaceutical grade deep sea fish oil, natural cherry flavoring and natural tocopherols.</p>
      <div class="usage">
        <p>SUGGESTED USE: As a dietary Supplement take one teaspoon daily, with food, or as directed by your health care professional.</p>
        <p>WARNINGS: Please consult your health care advisor if you are taking blood thinners or are diabetic</p>
      </div>
    </div>
    <div class="claim">100% FRUIT &amp; VEGETABLE<br>NO PRESEVANCE ON ADORMIs</div>
    <div class="front">
      <svg width="560" height="478" viewBox="0 0 560 478" aria-hidden="true">
        <defs><linearGradient id="swoosh1" x1="0" y1="0" x2="1" y2="1"><stop offset="0" stop-color="#ffe57a"/><stop offset="1" stop-color="#f4a21a"/></linearGradient></defs>
        <path d="M0 478 C150 420 320 385 560 362 L560 478 Z" fill="url(#swoosh1)"/>
        <path d="M0 462 C170 400 330 368 560 348" stroke="#ffffff" stroke-width="14" fill="none"/>
        <path d="M0 446 C170 384 330 352 560 333" stroke="#f08a1a" stroke-width="8" fill="none"/>
      </svg>
      <div class="fruit" role="img" aria-label="Illustration of fresh carrots and a cut mango" style="left:15px;top:250px;width:300px;height:200px;border-radius:50% 40% 30% 50%;background:radial-gradient(circle at 55% 55%,#ffc531,#f27a1c 70%)"></div>
      <div class="badge-new">New</div>
      <div class="brand">frutalia</div>
      <div class="flavour">carrot<br>mango</div>
      <div class="seal" role="img" aria-label="Quality seal"></div>
    </div>
    <div class="benefits">
      <h2>5 BENEFITS OF<br>MANGO &amp; CARROT</h2>
      <ul>
        <li>Helps prevent cancer</li>
        <li>Promotes healthy eyes</li>
        <li>Helps to keep skin young</li>
        <li>Improves the functioning of the immune system</li>
        <li>Promotes the functioning of the brain</li>
      </ul>
      <p class="serve">Shake well before<br>to serve fresh</p>
      <svg class="bin" viewBox="0 0 58 86" role="img" aria-label="Dispose in bin"><rect x="2" y="34" width="36" height="50" rx="3" fill="#fff"/><rect x="0" y="28" width="40" height="6" fill="#fff"/><rect x="42" y="6" width="12" height="78" rx="5" fill="#fff"/></svg>
      <p class="maker">Manufactured by<br>FRUTALIA<br>USA<br>Ph.: + 1 555 0186<br>www.frutalia.com</p>
    </div>
  </section>

  <!-- label variant 2 -->
  <section class="label label--two">
    <div class="info">
      <div class="facts">
        <h2>Supplement Facts</h2>
        <div class="row top"><span>Serving size 1 teaspoon (5ml)</span><span>Servings per container 45</span></div>
        <div class="row head"><span>Amount per Serving</span><span>% Daily Value</span></div>
        <div class="row"><span>Calories</span><span>40</span><span></span></div>
        <div class="row"><span>Calories from Fat</span><span>40</span><span></span></div>
        <div class="row"><span>Total Fat</span><span>4.5g</span><span>7.0%*</span></div>
        <div class="row indent"><span>Saturated Fat</span><span>1.0g</span><span>5.0%*</span></div>
        <div class="row indent"><span>Polyunsaturated Fat</span><span>2.0g</span><span>*</span></div>
        <div class="row indent"><span>Monounsaturated Fat</span><span>1.0g</span><span>*</span></div>
        <div class="row"><span>Cholesterol</span><span>15mg</span><span>5.0%*</span></div>
        <div class="row"><span>Total Frutalia Fatty Acids</span><span class="wide">1400-1700 mg</span></div>
        <div class="row indent"><span>Eicosapentaenoic Acid (EPA)</span><span class="wide">740-825 mg</span></div>
        <div class="row indent"><span>Docosahexaenoic Acid (DHA)</span><span class="wide">460-550 mg</span></div>
        <div class="row indent"><span>Other Frutalia Fatty Acids</span><span class="wide">200-325 mg</span></div>
        <p class="note">*Percent daily values are based on a 2000 calorie diet.<br>Daily value not established.</p>
      </div>
      <p class="ingredients">INGREDIENTS: purified, molecularly-distilled pharmaceutical grade deep sea fish oil, natural cherry flavoring and natural tocopherols.</p>
      <div class="usage">
        <p>SUGGESTED USE: As a dietary Supplement take one teaspoon daily, with food, or as directed by your health care professional.</p>
        <p>WARNINGS: Please consult your health care advisor if you are taking blood thinners or are diabetic</p>
      </div>
    </div>
    <div class="claim">100% FRUIT &amp; VEGETABLE<br>NO PRESEVANCE ON ADORMIs</div>
    <div class="front">
      <svg width="560" height="478" viewBox="0 0 560 478" aria-hidden="true">
        <defs><linearGradient id="swoosh2" x1="0" y1="0" x2="1" y2="1"><stop offset="0" stop-color="#ffe57a"/><stop offset="1" stop-color="#f4a21a"/></linearGradient></defs>
        <path d="M0 478 C150 420 320 385 560 362 L560 478 Z" fill="url(#swoosh2)"/>
        <path d="M0 462 C170 400 330 368 560 348" stroke="#ffffff" stroke-width="14" fill="none"/>
        <path d="M0 446 C170 384 330 352 560 333" stroke="#f08a1a" stroke-width="8" fill="none"/>
      </svg>
      <div class="fruit" role="img" aria-label="Illustration of fresh carrots and a cut mango" style="left:15px;top:250px;width:300px;height:200px;border-radius:50% 40% 30% 50%;background:radial-gradient(circle at 55% 55%,#ffc531,#f27a1c 70%)"></div>
      <div class="badge-new">New</div>
      <div class="brand">frutalia</div>
      <div class="flavour">carrot<br>mango</div>
      <div class="seal" role="img" aria-label="Quality seal"></div>
    </div>
    <div class="benefits">
      <h2>5 BENEFITS OF<br>MANGO &amp; CARROT</h2>
      <ul>
        <li>Helps prevent cancer</li>
        <li>Promotes healthy eyes</li>
        <li>Helps to keep skin young</li>
        <li>Improves the functioning of the immune system</li>
        <li>Promotes the functioning of the brain</li>
      </ul>
      <p class="serve">Shake well before<br>to serve fresh</p>
      <svg class="bin" viewBox="0 0 58 86" role="img" aria-label="Dispose in bin"><rect x="2" y="34" width="36" height="50" rx="3" fill="#2f5a27"/><rect x="0" y="28" width="40" height="6" fill="#2f5a27"/><rect x="42" y="6" width="12" height="78" rx="5" fill="#2f5a27"/></svg>
      <p class="maker">Manufactured by<br>FRUTALIA<br>USA<br>Ph.: + 1 555 0186<br>www.frutalia.com</p>
    </div>
  </section>

  <!-- label variant 3 -->
  <section class="label label--three">
    <div class="info">
      <div class="facts">
        <h2>Supplement Facts</h2>
        <div class="row top"><span>Serving size 1 teaspoon (5ml)</span><span>Servings per container 45</span></div>
        <div class="row head"><span>Amount per Serving</span><span>% Daily Value</span></div>
        <div class="row"><span>Calories</span><span>40</span><span></span></div>
        <div class="row"><span>Calories from Fat</span><span>40</span><span></span></div>
        <div class="row"><span>Total Fat</span><span>4.5g</span><span>7.0%*</span></div>
        <div class="row indent"><span>Saturated Fat</span><span>1.0g</span><span>5.0%*</span></div>
        <div class="row indent"><span>Polyunsaturated Fat</span><span>2.0g</span><span>*</span></div>
        <div class="row indent"><span>Monounsaturated Fat</span><span>1.0g</span><span>*</span></div>
        <div class="row"><span>Cholesterol</span><span>15mg</span><span>5.0%*</span></div>
        <div class="row"><span>Total Frutalia Fatty Acids</span><span class="wide">1400-1700 mg</span></div>
        <div class="row indent"><span>Eicosapentaenoic Acid (EPA)</span><span class="wide">740-825 mg</span></div>
        <div class="row indent"><span>Docosahexaenoic Acid (DHA)</span><span class="wide">460-550 mg</span></div>
        <div class="row indent"><span>Other Frutalia Fatty Acids</span><span class="wide">200-325 mg</span></div>
        <p class="note">*Percent daily values are based on a 2000 calorie diet.<br>Daily value not established.</p>
      </div>
      <p class="ingredients">INGREDIENTS: purified, molecularly-distilled pharmaceutical grade deep sea fish oil, natural cherry flavoring and natural tocopherols.</p>
      <div class="usage">
        <p>SUGGESTED USE: As a dietary Supplement take one teaspoon daily, with food, or as directed by your health care professional.</p>
        <p>WARNINGS: Please consult your health care advisor if you are taking blood thinners or are diabetic</p>
      </div>
    </div>
    <div class="claim">100% FRUIT &amp; VEGETABLE<br>NO PRESEVANCE ON ADORMIs</div>
    <div class="front">
      <div class="fruit" role="img" aria-label="Illustration of fresh carrots and a cut mango" style="left:20px;top:340px;width:230px;height:138px;border-radius:50% 50% 0 0;background:radial-gradient(circle at 50% 70%,#ffc531,#f27a1c 70%)"></div>
      <div class="badge-new">New</div>
      <div class="brand">frutalia</div>
      <div class="flavour">Carrot Mango</div>
      <div class="seal" role="img" aria-label="Quality seal"></div>
    </div>
    <div class="benefits">
      <h2>5 BENEFITS OF<br>MANGO &amp; CARROT</h2>
      <ul>
        <li>Helps prevent cancer</li>
        <li>Promotes healthy eyes</li>
        <li>Helps to keep skin young</li>
        <li>Improves the functioning of the immune system</li>
        <li>Promotes the functioning of the brain</li>
      </ul>
      <p class="serve">Shake well before<br>to serve fresh</p>
      <svg class="bin" viewBox="0 0 58 86" role="img" aria-label="Dispose in bin"><rect x="2" y="34" width="36" height="50" rx="3" fill="#7cb43a"/><rect x="0" y="28" width="40" height="6" fill="#7cb43a"/><rect x="42" y="6" width="12" height="78" rx="5" fill="#7cb43a"/></svg>
      <p class="maker">Manufactured by<br>FRUTALIA<br>USA<br>Ph.: + 1 555 0186<br>www.frutalia.com</p>
    </div>
  </section>

</div>
</body>
</html>
```